Corporate Business Card Design Project

..Hi designers!
I have established a consultancy within strategic communnications, for which I need a business card design - I've seen some of the things you do in here, and they're great! I'll provide some information in the following:
Name: BriarLedger
Tagline: Guiding Dialogue
Service: Strategic communications consulting (primariy internal communication and optimizing): various organisations - e.g. SMEs, NGOs and NPOs - are offered an analysis of their current efforts and, on the basis of that, management consulting tailored their unique challenges and needs.
It's a sole proprietorship - for now! - but it's my plan to employ 5-20 persons over the years. Therefore the card should NOT symbolize a start-up, but communicate a well-established, serious consultancy. Hence, it should also apply to serious companies and organizations - think Veltra or Hollis Brant Group (both as sender and receiver) ;)
The design should accordingly have a formal, conservative, stylish, corporate, clean look! and ditto colors, eg. black, grey, white etc - corresponding to the logo. The only colour that can appear is the same orange contrast as in my logo (see attachement). Not too bold or dramatic fonds or letters.
I choose the double sided as I think it gives the most professional look: One side with name, titel, phone, e-mail - then a little space - and four additional lines for address.
This composition is if all information should be in the same "column" - feel free to provide suggestions with the address places elsewhere on the one side.
On the other side, I'm only thinkin' something with the logo.
I'd be happy to see different ideas re. the use of the orange contrast, placement of logo, etc.
I do not plan on changing the design of businees cards ever - as I think it is more serious keeping a concept and avoid rebranding - and I'm sure that you can deliver an ever-lasting logo for my company! Thanks :).
Let's play the rest by ear in the correspondance.
Target Market(s)
Executive level: CEOs, HR directors, communication managers/directors, business owners.
Industry/Entity Type
Management Consulting

```html
<!DOCTYPE html>
<html lang="en">
<head>
<meta charset="utf-8">
<title>BriarLedger – Business Card</title>
<link rel="stylesheet" href="https://fonts.googleapis.com/css2?family=Crimson+Text:wght@400&display=swap">
<style>
  :root {
    --paper: #ffffff;
    --ink: #111111;
    --ink-soft: #5a5a5a;
    --ink-muted: #6b6b6b;
    --accent: #e8901e;
  }
  * { margin: 0; padding: 0; box-sizing: border-box; }
  html, body {
    width: 1200px;
    height: 709px;
    overflow: hidden;
    background: var(--paper);
  }
  .card {
    position: relative;
    width: 1200px;
    height: 709px;
    background: var(--paper);
    font-family: "Crimson Text", "Palatino Linotype", Georgia, serif;
    color: var(--ink-soft);
  }
  .brand {
    position: absolute;
    left: 89px;
    top: 106px;
  }
  .brand-name {
    display: flex;
    align-items: center;
    gap: 12px;
    font-size: 58px;
    font-weight: 400;
    line-height: 1;
    color: var(--ink);
  }
  .brand-mark {
    width: 11px;
    height: 11px;
    background: var(--accent);
    flex: none;
  }
  .brand-tagline {
    margin-top: 0;
    margin-left: 158px;
    font-size: 11px;
    letter-spacing: 3px;
    color: var(--ink-muted);
  }
  .person {
    position: absolute;
    left: 0;
    right: 0;
    top: 268px;
    text-align: center;
  }
  .person-name {
    font-size: 90px;
    font-weight: 400;
    line-height: 1;
    color: var(--ink);
    margin-left: 36px;
  }
  .person-title {
    margin-top: 0;
    font-size: 44px;
    line-height: 1;
    color: var(--ink-soft);
    margin-left: 36px;
  }
  .contact {
    position: absolute;
    font-style: normal;
    font-size: 22px;
    line-height: 27.5px;
    color: var(--ink-soft);
  }
  .contact-main { left: 113px; top: 503px; }
  .contact-offices { left: 705px; top: 498px; }
  .contact-main .label { display: inline-block; width: 81px; }
  .contact-line.indent { padding-left: 81px; }
</style>
</head>
<body>
  <main class="card">
    <header class="brand">
      <div class="brand-name">BriarLedger<span class="brand-mark"></span></div>
      <div class="brand-tagline">Guiding Dialogue</div>
    </header>

    <section class="person">
      <h1 class="person-name">Owen Hartley</h1>
      <p class="person-title">Consultant</p>
    </section>

    <address class="contact contact-main">
      <div class="contact-line"><span class="label">Adress:</span>Linden Avenue 48,</div>
      <div class="contact-line indent">4816 Carrow Bay</div>
      <div class="contact-line"><span class="label">Phone:</span>5553019476</div>
      <div class="contact-line"><span class="label">E-mail:</span>owenhartley@briarledger.com</div>
    </address>

    <address class="contact contact-offices">
      <div class="contact-line">adress: Cedar Avenue 9041, Houston, TX</div>
      <div class="contact-line">adress: Birch Avenue 9315, Denver, CO</div>
      <div class="contact-line">adress: Elm Avenue 7624, Albany, NY</div>
      <div class="contact-line">adress: Alder Street 57, Helena, MT</div>
    </address>
  </main>
</body>
</html>
```